Business Cards for a Junk Removal Company

Hello,
We are looking to have business cards designed that are simple, bold, easy to read, and right to the point. Please see the attachments for our logo files. We want the card to be yellow on both sides ( Color code Yellow: #FFE01B). The logo text font is (Rockstar Extra Bold) and this is also in the files attached. Please make the text black for the logo. On the back side of the card, you can use white and black for text. Thank you in advance for your hard work!

Front of card-
Harbor Haul Removal (logo)
Back of card-
Harbor Haul Removal
Donate - Recycle - Dispose
518-276-9053
www.harborhaulremoval.example
info@harborhaulremoval.example

Industry/Entity Type

Junk removal

Contact Information for Business Card

FRONT OF CARD- Harbor Haul Removal (logo) BACK OF CARD- Harbor Haul Removal Donate - Recycle - Dispose 518-276-9053 www.harborhaulremoval.example info@harborhaulremoval.example

Font styles to use
Other font styles liked:
• Rockstar Extra Bold

Colors
FFF300
FFF600
FEFA6F
FFFEC7
FFFEE8

Requirements
Must have
• Must have color code Yellow: #FFE01B for the background of front and back of the card

```html
<!DOCTYPE html>
<html lang="en">
<head>
<meta charset="utf-8">
<title>Harbor Haul Removal — Business Cards</title>
<link href="https://fonts.googleapis.com/css2?family=Roboto+Slab:wght@400;800&display=swap" rel="stylesheet">
<style>
  :root {
    --card-yellow: #FFE01B;
    --ink: #000000;
    --backdrop: #d6d6d6;
    --card-w: 540px;
    --card-h: 309px;
  }
  * { margin: 0; padding: 0; box-sizing: border-box; }
  html, body {
    width: 1200px; height: 913px; overflow: hidden;
    background: var(--backdrop);
    font-family: "Roboto Slab", Georgia, serif;
    color: var(--ink);
  }
  .stage {
    width: 1200px; height: 913px;
    display: flex; align-items: center; justify-content: center; gap: 40px;
  }
  .card {
    position: relative;
    width: var(--card-w); height: var(--card-h);
    background: var(--card-yellow);
    border: 2px solid var(--ink);
  }

  /* Info side */
  .card-info .brand-name {
    position: absolute; top: 42px; left: 0; right: 0;
    text-align: center;
    font-weight: 800; font-size: 40px; line-height: 1; letter-spacing: -0.5px;
  }
  .card-info .tagline {
    position: absolute; top: 112px; left: 0; right: 0;
    text-align: center;
    font-weight: 800; font-size: 22px;
  }
  .card-info .divider-long {
    position: absolute; top: 160px; left: 150px; right: 28px;
    height: 1px; background: var(--ink);
  }
  .card-info .person {
    position: absolute; left: 30px; top: 168px;
  }
  .person-name { font-weight: 800; font-size: 22px; line-height: 1.1; }
  .person-title { font-size: 13px; margin-top: 2px; }
  .divider-short { width: 130px; height: 1px; background: var(--ink); margin: 8px 0 8px; }
  .contact-list { list-style: none; font-size: 13px; }
  .contact-list li { display: flex; align-items: center; gap: 8px; line-height: 20px; }
  .contact-list svg { width: 13px; height: 13px; flex: none; }

  /* Logo side */
  .card-logo { display: flex; align-items: center; justify-content: center; }
  .card-logo .brand-name {
    font-weight: 800; font-size: 54px; line-height: 1.05;
    text-align: center; letter-spacing: -0.5px;
  }
</style>
</head>
<body>
<main class="stage">
  <section class="card card-info" aria-label="Card back with contact details">
    <div class="brand-name">Harbor Haul Removal</div>
    <div class="tagline">Donate - Recycle - Dispose</div>
    <div class="divider-long"></div>
    <div class="person">
      <div class="person-name">Daniel Reyes</div>
      <div class="person-title">managing director</div>
      <div class="divider-short"></div>
      <ul class="contact-list">
        <li>
          <svg viewBox="0 0 16 16" aria-hidden="true"><path d="M4 1.5l2.5 3-1.5 1.5c.8 1.8 2.2 3.2 4 4l1.5-1.5 3 2.5-1.5 2.5C7 13.5 2.5 9 1.5 3z" fill="var(--ink)"/></svg>
          518-276-9053
        </li>
        <li>
          <svg viewBox="0 0 16 16" aria-hidden="true"><rect x="1" y="3" width="14" height="10" fill="var(--ink)"/><path d="M1.5 3.5L8 9l6.5-5.5" stroke="var(--card-yellow)" stroke-width="1.4" fill="none"/></svg>
          info@harborhaulremoval.example
        </li>
        <li>
          <svg viewBox="0 0 16 16" aria-hidden="true"><circle cx="8" cy="8" r="7" fill="var(--ink)"/><g stroke="var(--card-yellow)" stroke-width="1" fill="none"><ellipse cx="8" cy="8" rx="3" ry="6.5"/><path d="M1.5 8h13M2.5 5h11M2.5 11h11"/></g></svg>
          www.harborhaulremoval.example
        </li>
      </ul>
    </div>
  </section>

  <section class="card card-logo" aria-label="Card front with company name">
    <div class="brand-name">Harbor Haul<br>Removal</div>
  </section>
</main>
</body>
</html>
```